Example of School Sign for Digital Siganage

We sell digital signage software and screens. I have an expo coming up and I want some examples of typical images and messages that a school might use on an outdoor screen for public viewing. The resolution of the screen is quite low at 504 pixels wide by 336 pixels high. This means that we cannot use anything too small or detailed. The images could however be created at 1008 x 672 and that way they will scale down. The images need to be delivered in .psd format with all layers available.

We will call the School Stonemeadow Academy. We want the school name on all the images (slides) and a fictitious logo associated with the name. Examples of the images required would be. . .

1. Congratulations to Lydia Pranter School Dux 2015. (This would have an image of a smiling teenage girl.)

2. Team of the Week. Year 10 Girls under 16 Soccer Team. 5-Wins 0-Losses. (This would have a picture of girls playing soccer.)

3. School Production of Tinsel. August 12th -17th. Get your tickets from the office . (An image of a Tinsel logo)

4. Car Wash at School the Sunday to raise funds for the Year 9 Singapore Trip. (Image of students washing a car)

5. School Holidays Start Friday the 8th of September. School re-opens Monday 25th of September. (An image of a crowd of happy students)

6. Student of the Week. Owen Blakely, Winner of the Frontier Machina Trophy. (image of teenage student with robot)

Hopefully this is clear.

Industry/Entity Type

Digital Signage

Font styles to use
Sans Serif

Requirements
Must have
• School Name and Logo
Should not have
• Any very small fonts or too much fine detail

```html
<!DOCTYPE html>
<html lang="en">
<head>
<meta charset="utf-8">
<title>Stonemeadow Academy – Digital Signage Slides</title>
<link rel="stylesheet" href="https://fonts.googleapis.com/css2?family=Open+Sans:wght@300;400;600;700;800&display=swap">
<style>
  :root {
    --sky: #29a9e1;
    --sky-deep: #1a93cf;
    --navy: #163f73;
    --brand: #1d4f86;
    --brand-accent: #2aa7df;
    --white: #ffffff;
    --page-top: #ffffff;
    --page-bottom: #7cc8ec;
  }
  * { margin: 0; padding: 0; box-sizing: border-box; }
  html, body { width: 1200px; height: 1000px; overflow: hidden; }
  body {
    font-family: "Open Sans", Arial, sans-serif;
    background:
      radial-gradient(ellipse 700px 260px at 0% 100%, var(--page-bottom), transparent 70%),
      radial-gradient(ellipse 700px 260px at 100% 100%, var(--page-bottom), transparent 70%),
      linear-gradient(to bottom, var(--page-top) 55%, #d6eef9 100%);
    position: relative;
  }
  .slide {
    position: absolute;
    overflow: hidden;
    background: var(--sky);
    box-shadow: 0 2px 6px rgba(0,0,0,0.25);
    color: var(--white);
  }
  .col-left { left: 240px; width: 368px; }
  .col-right { left: 620px; width: 372px; }
  .row-1 { top: 48px; height: 247px; }
  .row-2 { top: 307px; height: 246px; }
  .row-3 { top: 566px; height: 245px; }

  .photo { position: absolute; top: 0; right: 0; bottom: 0; }
  .copy { position: absolute; left: 0; top: 0; text-align: center; }
  .headline { font-weight: 300; line-height: 0.95; text-transform: uppercase; }
  .kicker { font-weight: 700; color: var(--navy); line-height: 1.0; font-size: 16px; }
  .detail { font-weight: 700; line-height: 1.02; font-size: 15px; }

  .brand-tab {
    position: absolute; left: 0; bottom: 0;
    width: 168px; height: 58px;
    background: var(--white);
    border-top-right-radius: 10px;
    display: flex; align-items: center; gap: 8px;
    padding-left: 12px;
  }
  .brand-mark { width: 14px; height: 14px; background: var(--brand-accent); flex: none; }
  .brand-name { font-weight: 600; color: var(--brand); font-size: 15px; line-height: 1.1; }

  .holidays .photo { width: 230px; background: linear-gradient(90deg, var(--sky) 0%, #7aa88f 25%, #c99a86 55%, #8a6c55 100%); }
  .holidays .copy { width: 180px; top: 20px; }
  .holidays .headline { font-size: 31px; }
  .holidays .detail { margin-top: 8px; }
  .holidays .detail + .detail { margin-top: 10px; }

  .team .photo { width: 190px; background: linear-gradient(90deg, var(--sky) 0%, #9cc39a 25%, #c9463e 55%, #5f9b4d 100%); }
  .team .copy { width: 200px; top: 18px; }
  .team .headline { font-size: 25px; margin-top: 6px; }
  .team .detail { font-size: 17px; margin-top: 10px; }

  .production {
    background: linear-gradient(165deg, var(--sky) 0%, var(--sky) 14%, #ffffff 42%, #ffffff 66%, #d3ecf8 82%, var(--sky) 100%);
  }
  .production .kicker-light {
    position: absolute; left: 16px; top: 18px;
    font-weight: 700; font-size: 15px; color: var(--white);
  }
  .production .show-logo {
    position: absolute; left: 18px; top: 44px; width: 336px; height: 118px;
    background: linear-gradient(135deg, #c21f2b 0%, #7fc6ec 45%, #e3283a 100%);
    border-radius: 14px;
  }
  .production .show-info { position: absolute; right: 12px; bottom: 20px; text-align: right; color: var(--navy); }
  .production .show-dates { font-weight: 700; font-size: 14px; }
  .production .show-note { font-weight: 400; font-size: 12px; margin-top: 2px; }

  .dux .photo { width: 200px; background: linear-gradient(90deg, var(--sky) 0%, #8b6a55 30%, #d6a98d 60%, #6b4a38 100%); }
  .dux .copy { width: 180px; top: 32px; }
  .dux .headline { font-size: 36px; margin-top: 6px; }
  .dux .detail { margin-top: 10px; }

  .student .photo { width: 210px; background: linear-gradient(90deg, var(--sky) 0%, #f0d6d6 30%, #e9b9a4 60%, #3c3c44 100%); }
  .student .copy { width: 180px; top: 16px; }
  .student .headline { font-size: 35px; margin-top: 4px; }
  .student .detail { font-size: 15px; line-height: 1.0; margin-top: 4px; }

  .carwash .photo { width: 200px; background: linear-gradient(90deg, var(--sky) 0%, #9fb6c4 30%, #e8d63a 60%, #8fa4b0 100%); }
  .carwash .copy { width: 200px; top: 28px; }
  .carwash .headline { font-size: 30px; }
  .carwash .detail { font-size: 17px; margin-top: 8px; }

  .brand-panel {
    position: absolute; left: 394px; top: 838px; width: 440px; height: 162px;
    background: var(--white);
    border-radius: 16px 16px 0 0;
    display: flex; align-items: center; justify-content: center; gap: 16px;
  }
  .brand-panel .brand-mark { width: 34px; height: 34px; }
  .brand-panel .brand-name { font-size: 34px; line-height: 1.1; }
</style>
</head>
<body>

  <section class="slide holidays col-left row-1">
    <div class="photo" role="img" aria-label="Photo of a group of happy students outdoors"></div>
    <div class="copy">
      <h2 class="headline">School<br>Holidays</h2>
      <p class="detail">Start Friday<br>8th of September</p>
      <p class="detail">School re-opens<br>Monday<br>25th September</p>
    </div>
    <div class="brand-tab"><span class="brand-mark"></span><span class="brand-name">Stonemeadow<br>Academy</span></div>
  </section>

  <section class="slide team col-right row-1">
    <div class="photo" role="img" aria-label="Photo of girls playing soccer"></div>
    <div class="copy">
      <p class="kicker">Team of<br>the Week</p>
      <h2 class="headline">Year 10 Girls<br>Under 16<br>Soccer Team</h2>
      <p class="detail">5-Wins 0-Losses</p>
    </div>
    <div class="brand-tab"><span class="brand-mark"></span><span class="brand-name">Stonemeadow<br>Academy</span></div>
  </section>

  <section class="slide production col-left row-2">
    <p class="kicker-light">School Production of</p>
    <div class="show-logo" role="img" aria-label="Tinsel show title logo artwork"></div>
    <div class="show-info">
      <p class="show-dates">August 12th -17th</p>
      <p class="show-note">Get your tickets from the office</p>
    </div>
    <div class="brand-tab"><span class="brand-mark"></span><span class="brand-name">Stonemeadow<br>Academy</span></div>
  </section>

  <section class="slide dux col-right row-2">
    <div class="photo" role="img" aria-label="Photo of a smiling teenage girl"></div>
    <div class="copy">
      <p class="kicker">Congratulations<br>to</p>
      <h2 class="headline">Lydia<br>Pranter</h2>
      <p class="detail">School Dux 2015</p>
    </div>
    <div class="brand-tab"><span class="brand-mark"></span><span class="brand-name">Stonemeadow<br>Academy</span></div>
  </section>

  <section class="slide student col-left row-3">
    <div class="photo" role="img" aria-label="Photo of a teenage student with his robot"></div>
    <div class="copy">
      <p class="kicker">Student<br>of the Week</p>
      <h2 class="headline">Owen<br>Blakely</h2>
      <p class="detail">Winner of the<br>Frontier Machina<br>Trophy</p>
    </div>
    <div class="brand-tab"><span class="brand-mark"></span><span class="brand-name">Stonemeadow<br>Academy</span></div>
  </section>

  <section class="slide carwash col-right row-3">
    <div class="photo" role="img" aria-label="Photo of a student washing a car"></div>
    <div class="copy">
      <h2 class="headline">Car Wash</h2>
      <p class="detail">at School the<br>Sunday to<br>raise funds for<br>the Year 9<br>Singapore Trip</p>
    </div>
    <div class="brand-tab"><span class="brand-mark"></span><span class="brand-name">Stonemeadow<br>Academy</span></div>
  </section>

  <div class="brand-panel">
    <span class="brand-mark"></span>
    <span class="brand-name">Stonemeadow<br>Academy</span>
  </div>

</body>
</html>
```